" Somos uma empresa afiliada a Lumira Capital e representamos ela em Cuiabá. Prestamos o serviço de assessoria em investimentos a clientes de alto poder aquisitivo, um público private. Serviço exclusivo de "

```html
<!DOCTYPE html>
<html lang="pt-BR">
<head>
<meta charset="UTF-8">
<title>Papel timbrado – Vento Investimentos</title>
<link href="https://fonts.googleapis.com/css2?family=Cormorant+Garamond:wght@500&family=Montserrat:wght@400;500&display=swap" rel="stylesheet">
<style>
  :root {
    --backdrop: #e4e5e7;
    --paper: #ffffff;
    --ink: #3b3631;
    --ink-soft: #8a8a8a;
    --gold-light: #e8d3a4;
    --gold: #b08b4f;
    --gold-deep: #5a4326;
    --partner-mark: #1a1a1a;
    --divider: #c9c9c9;
  }
  * { margin: 0; padding: 0; box-sizing: border-box; }
  html, body {
    width: 1200px; height: 1200px; overflow: hidden;
    background: var(--backdrop);
  }
  .letterhead {
    position: absolute;
    left: 204px; top: 34px;
    width: 792px; height: 1132px;
    background: var(--paper);
    box-shadow: 0 10px 30px rgba(0,0,0,0.12);
    font-family: "Montserrat", sans-serif;
  }
  .brand {
    position: absolute;
    top: 74px; left: 0; right: 0;
    display: flex; justify-content: center; align-items: center; gap: 12px;
  }
  .brand-square {
    width: 26px; height: 26px; background: var(--gold);
  }
  .brand-name {
    font-family: "Cormorant Garamond", serif;
    font-weight: 500;
    font-size: 30px;
    letter-spacing: 2px;
    color: var(--ink);
  }
  .contact-list {
    position: absolute;
    left: 52px; top: 930px;
    list-style: none;
    font-size: 10px;
    color: var(--ink-soft);
    line-height: 1.35;
  }
  .contact-item {
    display: flex; align-items: flex-start; gap: 8px;
    margin-bottom: 9px;
  }
  .contact-icon { width: 14px; height: 14px; flex: none; }
  .footer-rule {
    position: absolute;
    left: 222px; top: 1036px;
    width: 400px; height: 5px;
    background: linear-gradient(90deg, var(--gold-light), var(--gold) 45%, var(--gold-deep));
  }
  .partner {
    position: absolute;
    left: 634px; top: 1004px;
    display: flex; align-items: center; gap: 10px;
  }
  .partner-badge {
    width: 36px; height: 36px; background: var(--partner-mark);
  }
  .partner-divider {
    width: 1px; height: 44px; background: var(--divider);
  }
  .partner-text {
    font-size: 9px;
    letter-spacing: 0.6px;
    text-transform: uppercase;
    color: var(--ink-soft);
    line-height: 1.35;
  }
</style>
</head>
<body>
  <main class="letterhead">
    <header class="brand">
      <span class="brand-square"></span>
      <span class="brand-name">VENTO INVESTIMENTOS</span>
    </header>

    <ul class="contact-list">
      <li class="contact-item">
        <svg class="contact-icon" viewBox="0 0 14 14"><circle cx="7" cy="7" r="6.3" fill="none" stroke="#3b3631" stroke-width="1"/><path d="M5 4.2l1.2 1.4-0.7 0.9c0.4 0.9 1.1 1.6 2 2l0.9-0.7 1.4 1.2-0.6 1c-2.6-0.3-4.6-2.3-4.9-4.9z" fill="#3b3631"/></svg>
        <span>(65) 3000-0000</span>
      </li>
      <li class="contact-item">
        <svg class="contact-icon" viewBox="0 0 14 14"><circle cx="7" cy="7" r="6.3" fill="none" stroke="#3b3631" stroke-width="1"/><path d="M7 3.3a2.4 2.4 0 0 1 2.4 2.4c0 1.8-2.4 4.6-2.4 4.6s-2.4-2.8-2.4-4.6A2.4 2.4 0 0 1 7 3.3z" fill="#3b3631"/><circle cx="7" cy="5.7" r="0.8" fill="#fff"/></svg>
        <span>Av. Central, 1200 – Sala 45<br>Cuiabá – MT</span>
      </li>
      <li class="contact-item">
        <svg class="contact-icon" viewBox="0 0 14 14"><circle cx="7" cy="7" r="6.3" fill="none" stroke="#3b3631" stroke-width="1"/><rect x="3.8" y="4.8" width="6.4" height="4.4" fill="none" stroke="#3b3631" stroke-width="0.9"/><path d="M3.8 4.8L7 7.3l3.2-2.5" fill="none" stroke="#3b3631" stroke-width="0.9"/></svg>
        <span>contato@ventoinvest.com.br</span>
      </li>
    </ul>

    <div class="footer-rule"></div>

    <div class="partner">
      <span class="partner-badge"></span>
      <span class="partner-divider"></span>
      <p class="partner-text">Agente autônomo<br>de investimentos<br>da Lumira Capital</p>
    </div>
  </main>
</body>
</html>
```